Web Design Project

Website Design Brief

Company Details
1a) Name of Company

FERNHOLLOW
1) What is the nature of your business?: Briefly describe your products or services:

INDEPENDENT CONTEMPORARY TRADITIONAL ITALIAN RESTAURANT IN THE HEART OF ST BARNABYS QUAY ALSO CATERING FOR PRIVATE CORPORATE EVENTS AND WEDDING RECEPTIONS

1a) Who is your target market? Who are you hoping to reach with your site?

CITY CORPORATES, LOCAL CORPORATES/BUSINESSES, LOCAL RESIDENTS, VISITORS TO THE DOCK, LOCAL HOTELS

Website Details
1b) Do you have an existing website? If so, what is the URL?
HTTP://WWW.FERNHOLLOWTRATTORIA.EXAMPLE

2b) IMPORTANT: Please list at least 3 URLs (web addresses) of high quality sites that you like the look of (these do not have to be sites who’s business is similar to yours. It aids us in determining what your design style is.) Please consider layout, colours, navigation, graphics, and typography.

http://www.thecorvell.example/

http://www.mordasque.example/

http://www.tivokitchen.example/

http://www.perzola.example/

3b) What colours or colour schemes would you like?

WHITE, BLACK, SILVER/ALUMINIUM (PLS LOOK AT OUR OUTSIDE CHAIRS)

4b) List the Navigation links for your Site:

5b) What type of look are you trying to achieve? (e.g. clean, high-tech, conservative, warm, flashy, etc.)

SIMPLE ELEGANT CLASSY INFORMATIVE, EASY TO USE, A REFLECTION OF THE BUSINESS ITSELF

6b) Please provide the addresses of competitors' sites, if possible:

Do not contact the client direct - all questions should go through Wendmoor Catering - info@wendmoorcatering.example
Updates

thanks for the designs that I have received so far. I have these general comments:

- please avoid using icons for phones or paperclips etc 
- use dummy text (one design used text from another website) 
- there won't any live social media feeds to the site
the client likes a lot of the designs that this company comes up with: 

i look forward to see some more designs

hi all, 

further to my last update, here are a few more pointers:
- there will be no search facilities - so no "search" box please 
- please just use the images supplied - no stock ones
- use just the page names give (no other pages) 

The client is looking for a simple, elegant design. 

Many thanks 
Neil 

thanks for all the designs. 

I have uploaded another file to the brief which shows some posters that the client particularly likes. Perhaps the homepage could consist of large rectangle made up of a number of boxes - for some introductory text, a large image, mailing list, contact details, Lunch Special etc - just an idea! 
It's clear that the client likes clean lines with square edges. 
I want to be able to pass the designs directly onto the client so can designers avoid adding extra info or page. For example one design has a tab for a "Gift Card" - it will be easier for me if such additions are avoided. 

thanks!                                                                                                                                                                                                                                                                                                                                                                                                    

Thank you for all your designs - please keep them coming! 

hi all,

I am meeting the client tomorrow afternoon so please submit revisions / designs before then. 

Many thanks, 
Neil

Target Market(s)

Business people, upmarket etc

Industry/Entity Type

Business

Requirements
Must have
• - The home page needs a slide show of images as well as:
- a mailing list form - very simple, "Join our mailing list - name, email"
- 3 or 4 sentences of text
- Friendwall link

```html
<!DOCTYPE html>
<html lang="en">
<head>
<meta charset="utf-8">
<title>Fernhollow Italian — Gallery</title>
<link rel="stylesheet" href="https://fonts.googleapis.com/css2?family=Crimson+Text:ital,wght@0,400;0,600;1,400&family=Great+Vibes&family=Arimo&display=swap">
<style>
  :root {
    --sidebar: #1d1d1d;
    --panel: rgba(28, 28, 28, 0.9);
    --rule: #3a3a3a;
    --gold: #c9a24a;
    --gold-soft: #b8953f;
    --text: #f1eee8;
    --muted: #8a8a8a;
    --field: #2e2e2e;
    --badge: #8d8d8d;
  }
  * { box-sizing: border-box; margin: 0; padding: 0; }
  html, body { width: 1200px; height: 750px; overflow: hidden; }
  body {
    position: relative;
    background: var(--sidebar);
    font-family: "Crimson Text", Georgia, serif;
    color: var(--text);
  }
  .lounge-photo {
    position: absolute; left: 357px; top: 0; width: 843px; height: 750px;
    background:
      radial-gradient(ellipse at 78% 55%, #d9a27a 0%, rgba(190,120,80,0.6) 25%, transparent 55%),
      linear-gradient(180deg, #2b2d35 0%, #4a4c58 30%, #6b3a24 55%, #3a1c12 100%);
  }
  .sidebar {
    position: absolute; left: 0; top: 0; width: 357px; height: 750px;
    background: var(--sidebar);
  }
  .brand {
    position: absolute; left: 33px; top: 18px; width: 273px; height: 92px;
    border-top: 2px solid var(--rule);
    border-bottom: 2px solid var(--rule);
    text-align: center;
  }
  .brand-name {
    display: block; margin-top: 12px;
    font-size: 34px; letter-spacing: 3px; color: var(--text);
  }
  .brand-tag {
    display: block; margin-top: 2px;
    font-size: 12px; letter-spacing: 4px; color: var(--text);
  }
  .main-nav { position: absolute; left: 33px; top: 110px; width: 273px; }
  .main-nav a {
    display: flex; align-items: center; height: 38.7px;
    border-bottom: 1px solid var(--rule);
    color: var(--text); text-decoration: none; font-size: 14px;
  }
  .main-nav a:last-child { border-bottom: 2px solid var(--rule); }
  .main-nav a.is-current { color: var(--gold); }
  .main-nav svg { margin: 0 9px 0 19px; }
  .newsletter-title {
    position: absolute; left: 41px; top: 391px;
    font-style: italic; font-size: 15px; color: var(--gold);
  }
  .newsletter-field {
    position: absolute; left: 40px; top: 417px; width: 200px; height: 35px;
    border-radius: 17px; background: var(--field);
    font-family: "Arimo", Arial, sans-serif; font-size: 8.5px; color: var(--muted);
    padding: 13px 0 0 13px;
  }
  .newsletter-submit {
    position: absolute; left: 253px; top: 424px;
    font-style: italic; font-size: 15px; color: var(--text);
    text-decoration: underline; text-underline-offset: 3px;
  }
  .promotions {
    position: absolute; left: 33px; top: 469px; width: 274px; height: 154px;
    border: 2px solid var(--rule); text-align: center;
  }
  .promotions h2 {
    margin-top: 4px; font-weight: 400; font-style: italic;
    font-size: 19px; letter-spacing: 0.5px; color: var(--gold);
  }
  .promotions p {
    text-align: left; margin: 4px 12px 0 25px;
    font-family: "Arimo", Arial, sans-serif; font-size: 8.5px; line-height: 15px;
  }
  .promotions p + p { margin-top: 15px; }
  .read-more {
    position: absolute; left: 86px; top: 118px; width: 87px; height: 25px;
    border-radius: 13px; background: var(--gold-soft);
    font-size: 12px; line-height: 25px; color: var(--text);
  }
  .follow {
    position: absolute; left: 53px; top: 634px;
    display: flex; align-items: center; gap: 10px;
  }
  .follow-label { font-style: italic; font-size: 13.5px; }
  .follow a { color: var(--gold); text-decoration: none; font-size: 15px; }
  .follow .divider { width: 1px; height: 14px; background: var(--rule); }

  .content {
    position: absolute; left: 358px; top: 0; width: 366px; height: 750px;
    background: var(--panel);
  }
  .page-header {
    position: absolute; left: 0; top: 18px; width: 366px; height: 93px;
    border-top: 2px solid var(--gold-soft);
    border-bottom: 2px solid var(--gold-soft);
    text-align: center;
  }
  .page-header h1 { margin-top: 26px; font-weight: 400; font-size: 31px; }
  .intro {
    position: absolute; left: 17px; top: 127px; width: 340px;
    font-family: "Arimo", Arial, sans-serif; font-size: 8.6px; line-height: 15px;
  }
  .hex {
    position: absolute; width: 96px; height: 108px;
    clip-path: polygon(50% 0, 100% 25%, 100% 75%, 50% 100%, 0 75%, 0 25%);
  }
  .hex.dish { background: radial-gradient(circle at 45% 40%, #9bb35a, #6d4a2a 60%, #2a2016); }
  .hex.kitchen { background: linear-gradient(135deg, #d8d4cc, #5c5a55 60%, #2a2a2a); }
  .hex.toast { background: linear-gradient(160deg, #2f8a9a, #b25a44 50%, #3a1a1a); }
  .hex.table { background: linear-gradient(180deg, #5a2c18, #b06a3a 60%, #e0c090); }
  .hex.diner { background: linear-gradient(150deg, #d8aaa2, #b57a74 60%, #4a2a24); }
  .hex.couple { background: linear-gradient(150deg, #3a3a3a, #d0b89a 50%, #1a1a1a); }

  .reservation-badge {
    position: absolute; left: 895px; top: -50px; width: 116px; height: 116px;
    border-radius: 50%; background: var(--badge);
    text-align: center; font-style: italic; font-size: 17px; line-height: 15px;
    padding-top: 62px; color: var(--text);
  }
</style>
</head>
<body>
  <div class="lounge-photo" role="img" aria-label="Warm lounge interior with cream leather sofas, candlelit glass table and tall windows onto the city"></div>

  <aside class="sidebar">
    <div class="brand">
      <span class="brand-name">Fernhollow</span>
      <span class="brand-tag">ITALIAN</span>
    </div>

    <nav class="main-nav">
      <a href="#"><svg width="14" height="8" viewBox="0 0 14 8"><path d="M0 4h13M9.5 0.5 13 4 9.5 7.5" stroke="#8a8a8a" fill="none"/></svg>Home</a>
      <a href="#"><svg width="14" height="8" viewBox="0 0 14 8"><path d="M0 4h13M9.5 0.5 13 4 9.5 7.5" stroke="#8a8a8a" fill="none"/></svg>Our Restaurant</a>
      <a href="#"><svg width="14" height="8" viewBox="0 0 14 8"><path d="M0 4h13M9.5 0.5 13 4 9.5 7.5" stroke="#8a8a8a" fill="none"/></svg>Our Menu</a>
      <a href="#" class="is-current"><svg width="14" height="8" viewBox="0 0 14 8"><path d="M0 4h13M9.5 0.5 13 4 9.5 7.5" stroke="#8a8a8a" fill="none"/></svg>Gallery</a>
      <a href="#"><svg width="14" height="8" viewBox="0 0 14 8"><path d="M0 4h13M9.5 0.5 13 4 9.5 7.5" stroke="#8a8a8a" fill="none"/></svg>Events</a>
      <a href="#"><svg width="14" height="8" viewBox="0 0 14 8"><path d="M0 4h13M9.5 0.5 13 4 9.5 7.5" stroke="#8a8a8a" fill="none"/></svg>Reservations</a>
      <a href="#"><svg width="14" height="8" viewBox="0 0 14 8"><path d="M0 4h13M9.5 0.5 13 4 9.5 7.5" stroke="#8a8a8a" fill="none"/></svg>Contact Us</a>
    </nav>

    <div class="newsletter-title">Newsletter</div>
    <div class="newsletter-field">Enter you email</div>
    <div class="newsletter-submit">Submit</div>

    <section class="promotions">
      <h2>Our Promotions</h2>
      <p>But I must explain to you how all this mistaken idea of denouncing pleasure and praising pain was borm</p>
      <p>and expound the actual teachings of the great explorer of the truth, the master-builder of human happiness.</p>
      <div class="read-more">Read More</div>
    </section>

    <div class="follow">
      <span class="follow-label">Follow us:</span>
      <a href="#">Friendwall</a>
      <span class="divider"></span>
      <a href="#">Quillpost</a>
    </div>
  </aside>

  <main class="content">
    <header class="page-header"><h1>Gallery</h1></header>
    <p class="intro">There are many variations of passages of Lorem Ipsum available, but the majority have suffered alteration in some form, by injected humour, or randomised words which don't look even slightly believable. If you are going to use a passage of Lorem Ipsum</p>

    <div class="hex dish" style="left:17px;top:206px" role="img" aria-label="Plated salad with raspberry"></div>
    <div class="hex kitchen" style="left:134px;top:206px" role="img" aria-label="Kitchen pan with vegetables"></div>
    <div class="hex toast" style="left:245px;top:206px" role="img" aria-label="Wine glasses raised in a toast"></div>
    <div class="hex table" style="left:17px;top:328px" role="img" aria-label="Set dining table with glasses"></div>
    <div class="hex diner" style="left:134px;top:328px" role="img" aria-label="Guest dining with a glass of wine"></div>
    <div class="hex couple" style="left:245px;top:328px" role="img" aria-label="Couple at dinner with white wine"></div>
    <div class="hex toast" style="left:17px;top:458px" role="img" aria-label="Wine glasses raised in a toast"></div>
    <div class="hex dish" style="left:134px;top:458px" role="img" aria-label="Plated salad with raspberry"></div>
    <div class="hex diner" style="left:245px;top:458px" role="img" aria-label="Guest dining with a glass of wine"></div>
  </main>

  <div class="reservation-badge">Reservation<br>Online</div>
</body>
</html>
```